The winning designer MUST include the open diamond between Barlow Tindell to be considered for finalization. We will not consider any designs that do not have the open diamond concept. If you need a link to the image, please email me at mark.barlow@barlowpartnerslaw.example
The front should display the image almost predominantly. Under the main image centered somewhere on the front side should have the website & blog or maybe just the website.
I want the back to have a smaller image of what is on the front, with the exception that the back will have all of the pertinent info such as:
Name -- centered
Office Number - bottom right
Fax - bottom right
email - bottom right
Address - bottom left
email - bottom left
blog - bottom left
https://files.quillmark.example/attachment/u/0/?id=7a3f92c1e4&view=att&ref=58b2c7d0e91f4a63&disp=inline
If this doesn't come out right, let me know and I can email it to you, as it is missing the diamond in the logo I uploaded.
Additionally, I want to see some different color variations in the background, but overall, I want the font and logo design to remain intact.
Marcus T. Barlow
Corwin Tindell
Title should be "Trial Attorney"

```html
<!DOCTYPE html>
<html lang="en">
<head>
<meta charset="utf-8">
<title>Barlow Tindell, PC — Business Card</title>
<link rel="stylesheet" href="https://fonts.googleapis.com/css2?family=Cinzel:wght@400&family=Raleway:wght@300;400&display=swap">
<style>
  :root {
    --page: #e6e6e4;
    --card: #ffffff;
    --ink: #6f6f6f;
    --ink-soft: #9a9a9a;
    --rule: #b9b9b9;
    --band: #4a4a4a;
    --band-text: #f2f2f2;
  }
  * { margin: 0; padding: 0; box-sizing: border-box; }
  html, body { width: 1200px; height: 901px; overflow: hidden; }
  body {
    background: var(--page);
    font-family: "Raleway", sans-serif;
    color: var(--ink);
    position: relative;
  }
  .card {
    position: absolute;
    left: 290px;
    width: 620px;
    height: 354px;
    background: var(--card);
    box-shadow: 0 6px 18px rgba(0,0,0,0.12);
    overflow: hidden;
  }
  .card--front { top: 62px; }
  .card--back { top: 478px; }

  /* Front */
  .firm-lockup {
    position: absolute;
    left: 110px;
    top: 112px;
    display: flex;
    align-items: center;
    gap: 18px;
  }
  .firm-lockup__square {
    width: 34px; height: 34px;
    background: var(--ink);
  }
  .firm-lockup__name {
    font-family: "Cinzel", serif;
    font-size: 38px;
    font-weight: 400;
    letter-spacing: 1px;
    color: var(--ink);
    white-space: nowrap;
  }
  .firm-rule {
    position: absolute;
    left: 162px; top: 170px;
    width: 350px; height: 1px;
    background: var(--rule);
  }
  .firm-tagline {
    position: absolute;
    left: 162px; top: 180px;
    width: 350px;
    text-align: center;
    font-family: "Cinzel", serif;
    font-size: 14px;
    letter-spacing: 5px;
    color: var(--ink);
  }
  .front-links {
    position: absolute;
    left: 162px; top: 236px;
    list-style: none;
    font-size: 11px;
    line-height: 19px;
    color: var(--ink-soft);
  }
  .front-links li { display: flex; align-items: center; gap: 8px; }
  .dot { width: 8px; height: 8px; border-radius: 50%; background: var(--ink); flex: none; }

  /* Back */
  .back-diagonal { position: absolute; inset: 0; }
  .back-band {
    position: absolute;
    left: 0; right: 0; bottom: 0; height: 120px;
    background: var(--band);
    clip-path: polygon(100% 0, 100% 100%, 0 100%, 0 92%);
  }
  .back-mark {
    position: absolute;
    left: 52px; top: 118px;
    display: flex; align-items: center; gap: 8px;
  }
  .back-mark__square { width: 14px; height: 14px; background: var(--ink); }
  .back-mark__name {
    font-family: "Cinzel", serif;
    font-size: 15px;
    color: var(--ink);
    white-space: nowrap;
  }
  .person {
    position: absolute;
    left: 176px; top: 62px;
    width: 200px;
    text-align: center;
  }
  .person__name { font-size: 22px; font-weight: 300; color: var(--ink); white-space: nowrap; }
  .person__title { font-size: 11px; letter-spacing: 1px; color: var(--ink-soft); margin-top: 4px; }
  .contact-list {
    position: absolute;
    left: 392px; top: 60px;
    width: 206px;
    list-style: none;
    font-size: 10px;
    line-height: 17px;
    color: var(--ink-soft);
    white-space: nowrap;
  }
  .contact-list li { display: flex; align-items: center; gap: 7px; }
  .contact-list svg { width: 9px; height: 9px; fill: var(--ink); flex: none; }
  .address {
    position: absolute;
    left: 52px; top: 222px;
    font-size: 11px;
    line-height: 17px;
    color: var(--ink-soft);
    white-space: nowrap;
  }
  .address a { color: inherit; text-decoration: none; }
  .band-site {
    position: absolute;
    right: 36px; bottom: 24px;
    font-size: 13px;
    letter-spacing: 0.5px;
    color: var(--band-text);
  }
</style>
</head>
<body>

<section class="card card--front" aria-label="Card front">
  <div class="firm-lockup">
    <span class="firm-lockup__square"></span>
    <span class="firm-lockup__name">Barlow Tindell, PC</span>
  </div>
  <div class="firm-rule"></div>
  <p class="firm-tagline">ATTORNEYS AT LAW</p>
  <ul class="front-links">
    <li><span class="dot"></span>www.barlowtindell.example</li>
    <li><span class="dot"></span>mark.barlow@barlowpartnerslaw.example</li>
  </ul>
</section>

<section class="card card--back" aria-label="Card back">
  <svg class="back-diagonal" width="620" height="354" viewBox="0 0 620 354" aria-hidden="true">
    <line x1="0" y1="205" x2="620" y2="140" stroke="#c4c4c4" stroke-width="1"/>
  </svg>
  <div class="back-band"></div>

  <div class="back-mark">
    <span class="back-mark__square"></span>
    <span class="back-mark__name">Barlow Tindell</span>
  </div>

  <div class="person">
    <p class="person__name">Marcus T. Barlow</p>
    <p class="person__title">Trial Attorney</p>
  </div>

  <ul class="contact-list">
    <li><svg viewBox="0 0 10 10"><path d="M2 0h2l1 3-1.5 1a6 6 0 0 0 2.5 2.5L7 5l3 1v2a2 2 0 0 1-2 2A8 8 0 0 1 0 2a2 2 0 0 1 2-2z"/></svg>212.555.0148</li>
    <li><svg viewBox="0 0 10 10"><rect x="0" y="3" width="10" height="6"/><rect x="2" y="0" width="6" height="3"/></svg>212.555.0149</li>
    <li><svg viewBox="0 0 10 10"><path d="M0 2h10v6H0z M0 2l5 3.5L10 2"/></svg>mark.barlow@barlowpartnerslaw.example</li>
    <li><svg viewBox="0 0 10 10"><circle cx="5" cy="5" r="5"/></svg>www.barlowtindell.example</li>
  </ul>

  <p class="address">
    48 Harbor Row, Suite 210<br>
    Lakeport, NY 10990<br>
    <a href="mailto:mark.barlow@barlowpartnerslaw.example">mark.barlow@barlowpartnerslaw.example</a>
  </p>

  <p class="band-site">www.barlowtindell.example</p>
</section>

</body>
</html>
```